Wageline Associates Business Card Design

We need a business card designed around our new logo. The business card should be modern in design & should communicate success, confidence, power, sophistication. The target market is young business professionals. This is for a human resource & payroll outsourcing business.

```html
<!DOCTYPE html>
<html lang="en">
<head>
<meta charset="utf-8">
<title>Wageline Associates Business Card</title>
<link href="https://fonts.googleapis.com/css2?family=Montserrat:wght@400;500;600&display=swap" rel="stylesheet">
<style>
  :root {
    --backdrop: #2b2b2b;
    --card-white: #ffffff;
    --card-dark: #232323;
    --ink: #2a2a2a;
    --accent-red: #e31e24;
    --bar-black: #0b0b0b;
  }
  * { margin: 0; padding: 0; box-sizing: border-box; }
  html, body {
    width: 1200px; height: 900px; overflow: hidden;
    background: var(--backdrop);
    font-family: "Montserrat", Arial, sans-serif;
  }
  .card {
    position: absolute; left: 261px; width: 656px;
    box-shadow: 0 6px 16px rgba(0,0,0,0.45);
  }
  .card-front { top: 69px; height: 357px; background: var(--card-white); color: var(--ink); }
  .card-back { top: 471px; height: 359px; background: var(--card-dark); }

  .brand-name {
    position: absolute; top: 38px; right: 32px;
    font-weight: 600; font-size: 26px; letter-spacing: 0.5px;
    color: var(--ink);
  }
  .holder { position: absolute; left: 26px; top: 177px; }
  .holder-name {
    font-weight: 500; font-size: 25px; letter-spacing: 1px;
    color: var(--accent-red); line-height: 1.1;
  }
  .holder-role { font-size: 16px; letter-spacing: 0.8px; margin-top: 4px; }
  .divider {
    position: absolute; left: 26px; right: 30px; top: 241px;
    height: 1.5px; background: var(--accent-red);
  }
  .contact-list {
    position: absolute; left: 26px; top: 263px; list-style: none;
    font-size: 16px; letter-spacing: 0.6px; line-height: 21px;
  }
  .contact-list li { display: flex; align-items: center; }
  .contact-list svg { width: 11px; height: 11px; margin-right: 7px; }
  .address {
    position: absolute; right: 30px; top: 284px; text-align: right;
    font-size: 16px; letter-spacing: 0.6px; line-height: 21px;
  }
  .edge-bar { position: absolute; bottom: 0; height: 9px; }
  .edge-bar.black { left: 0; width: 326px; background: var(--bar-black); }
  .edge-bar.red { left: 330px; right: 0; background: var(--accent-red); }

  .back-brand {
    position: absolute; left: 0; right: 0; top: 150px; text-align: center;
    font-weight: 600; font-size: 40px; letter-spacing: 1px;
    color: var(--card-white);
  }
</style>
</head>
<body>
  <section class="card card-front">
    <div class="brand-name">Wageline Associates</div>
    <div class="holder">
      <div class="holder-name">DANIEL ROURKE</div>
      <div class="holder-role">Director</div>
    </div>
    <div class="divider"></div>
    <ul class="contact-list">
      <li>
        <svg viewBox="0 0 12 12"><path d="M3 1 L5 3.5 L4 5 Q5 7 7 8 L8.5 7 L11 9 L9.5 11 Q5 11 1 3 Z" fill="var(--accent-red)"/></svg>
        412-555-0148
      </li>
      <li>
        <svg viewBox="0 0 12 12"><rect x="1" y="2.5" width="10" height="7" fill="none" stroke="var(--accent-red)" stroke-width="1.3"/><path d="M1 3 L6 6.5 L11 3" fill="none" stroke="var(--accent-red)" stroke-width="1.3"/></svg>
        info@wagelineassoc.com
      </li>
      <li>
        <svg viewBox="0 0 12 12"><g fill="none" stroke="var(--accent-red)" stroke-width="1"><circle cx="6" cy="6" r="5"/><ellipse cx="6" cy="6" rx="2.2" ry="5"/><path d="M1 6 H11 M2 3.5 H10 M2 8.5 H10"/></g></svg>
        www.wagelineassoc.com
      </li>
    </ul>
    <div class="address">2710 Ridgeview Pike,<br>Suite E Carnegie Falls, PA 15190</div>
    <div class="edge-bar black"></div>
    <div class="edge-bar red"></div>
  </section>

  <section class="card card-back">
    <div class="back-brand">Wageline Associates</div>
  </section>
</body>
</html>
```